Indian Takeaway Menu -

I would like to have double parallel fold A4 sheet menu.
A4 sheet cut in half and attached to the other half to make the sheet 4 small pages long.

Colors
abd036
ffffff

Requirements
Must have
• Please check new attachments - menu size and layout is not correct.
• I would like to add Dark brown colour. A4 sheet folded 4x Menu layout pocket size.
Nice to have
• Dark Brown - Parrot Green and very light Brown

```html
<!DOCTYPE html>
<html lang="en">
<head>
<meta charset="utf-8">
<title>Saffron Hearth – Takeaway Menu</title>
<link href="https://fonts.googleapis.com/css2?family=Source+Sans+3:ital,wght@0,400;0,600;0,700;1,600&family=Montserrat:wght@700&display=swap" rel="stylesheet">
<style>
:root{
  --bg:#8f8466;
  --paper:#ffffff;
  --green:#76962c;
  --amber:#f4b400;
  --red:#d4262e;
  --ink:#1f1f1f;
  --photo-dark:#5a3a22;
  --photo-warm:#c9882c;
}
*{box-sizing:border-box;margin:0;padding:0}
html,body{width:1200px;height:1200px;overflow:hidden}
body{background:var(--bg);font-family:"Source Sans 3",Arial,sans-serif;color:var(--ink);position:relative}
.sheet{position:absolute;left:203px;width:795px;height:562px;background:var(--paper);overflow:hidden}
.sheet--outside{top:30px}
.sheet--inside{top:615px}
.abs{position:absolute}
.bar{position:absolute;color:#fff;font-weight:600;font-size:9.5px;display:flex;align-items:center;justify-content:center;text-align:center;letter-spacing:.2px;line-height:1.35}
.bar--green{background:var(--green)}
.bar--amber{background:var(--amber)}
.bar--red{background:var(--red)}
.col{position:absolute;display:flex;flex-direction:column;justify-content:space-between}
.item{font-size:6.3px;line-height:1.38}
.item .head{display:flex;justify-content:space-between;font-weight:700}
.item p{text-align:justify}
.photo{position:absolute}
.price-list{position:absolute;list-style:none;font-size:6.3px;display:flex;flex-direction:column;justify-content:space-between}
.price-list li{display:flex;align-items:baseline}
.price-list .dots{flex:1;border-bottom:1px dotted #555;margin:0 3px;transform:translateY(-2px)}
.price-list b{width:22px;text-align:right}
.cover{position:absolute;left:405px;top:7px;width:382px;height:548px}
.brand{position:absolute;left:104px;top:8px;width:175px;height:70px;background:#fff;display:flex;flex-direction:column;align-items:center;justify-content:center}
.brand__name{font-weight:700;font-size:24px;color:var(--ink);line-height:1}
.brand__tag{font-size:5.5px;letter-spacing:1.4px;margin-top:3px}
.phone{position:absolute;left:0;width:382px;top:495px;text-align:center;font-family:"Montserrat",sans-serif;font-weight:700;color:#fff;font-size:19px;letter-spacing:2.5px}
.web{position:absolute;left:0;width:382px;top:522px;text-align:center;color:#fff;font-size:11px;letter-spacing:2px}
.band{position:absolute;left:0;width:795px;background:var(--red)}
.hours{left:17px;top:90px;width:180px;font-size:6.5px;line-height:1.4}
.hours h4{font-weight:700;font-size:6.5px}
.hours em{font-weight:600}
.allergens{left:17px;top:144px;width:185px;font-size:6.3px;font-weight:700;line-height:1.75}
.deals{left:10px;top:183px;width:181px;height:349px;background:var(--amber)}
.deals__inner{position:absolute;left:5px;top:5px;width:171px;height:174px;background:#fff}
.deals__title{position:absolute;left:23px;top:0;width:130px;height:28px;background:var(--amber);color:#fff;text-align:center;font-weight:700;line-height:1.1}
.deals__title span{display:block;font-size:8.5px;padding-top:2px}
.deals__title strong{font-size:13px}
.deals__intro{position:absolute;left:8px;top:36px;font-size:6.3px;font-weight:700;line-height:1.4}
.deals__list{position:absolute;left:8px;top:62px;width:156px;height:108px}
.set{position:absolute;left:7px;width:167px;font-size:6.3px;line-height:1.38}
.set .head{display:flex;justify-content:space-between;font-weight:700}
.set .cols{display:flex;color:#fff}
.set .cols div:first-child{width:103px}
.legend{left:202px;top:494px;font-size:8.5px;font-style:italic;font-weight:600;color:var(--green);line-height:1.5}
</style>
</head>
<body>

<section class="sheet sheet--outside">
  <div class="photo" style="left:17px;top:9px;width:363px;height:58px;background:linear-gradient(90deg,#4a5056 0%,#6b6f72 40%,#c3562a 62%,#e3b54a 85%,#7a6a55 100%)" role="img" aria-label="Photo of curry bowls and rice on a wooden table"></div>

  <div class="bar bar--green" style="left:12px;top:73px;width:187px;height:32px">PRAWN DISHES</div>
  <div class="col" style="left:12px;top:110px;width:187px;height:175px">
    <div class="item"><div class="head"><span>Prawn Masala 3</span><span>€11.95</span></div><p>Prawns in a smooth creamy sauce flavoured with kasoori methi &amp; tandoori spices.</p></div>
    <div class="item"><div class="head"><span>Prawn Karahi</span><span>€11.95</span></div><p>Prawns cooked with peppers, spring onion, Caramelised onion ,tomatoes &amp; whole spices.</p></div>
    <div class="item"><div class="head"><span>Goan Prawn Curry 3,4,5</span><span>€11.95</span></div><p>Fisherman`s favourite prawn curry aromatic with coconut , mustard , nuts ,curryleaves and spices from goa's costal area.</p></div>
    <div class="item"><div class="head"><span>Prawn Bhuna LF</span><span>€11.95</span></div><p>Prawns cooked in onions &amp; tomato with black pepper to bought together the kick of spices.</p></div>
    <div class="item"><div class="head"><span>Prawn Biryani 3,6,y</span><span>€11.95</span></div><p>Pan fried prawn cooked with egg, green peas &amp; onion served with curry sauce.</p></div>
  </div>

  <div class="bar bar--green" style="left:12px;top:292px;width:187px;height:32px">LAMB DISHES</div>
  <div class="col" style="left:12px;top:329px;width:187px;height:216px">
    <div class="item"><div class="head"><span>Lamb Madras</span><span>€10.95</span></div><p>The popular dish of madras cooked with plum tomato, degi chilli , coconut and finished with hint of lemon juice.</p></div>
    <div class="item"><div class="head"><span>Palak Gosht 3, y</span><span>€10.95</span></div><p>Pan-fried lamb pieces cooked with spinach, fresh herbs, ginger and touch of cream</p></div>
    <div class="item"><div class="head"><span>Lamb Roganjosh</span><span>€10.95</span></div><p>Slow cooked tender lamb in kashmiri style with fresh herbs and Himalayan spices.</p></div>
    <div class="item"><div class="head"><span>Lamb Kohlapuri 3,4,5</span><span>€10.95</span></div><p>Lamb dish from South Coast of India Flavoured with yoghurt, nuts and coconut.</p></div>
    <div class="item"><div class="head"><span>Lamb Jalferzi 3,5</span><span>€10.95</span></div><p>Lamb, tossed with cubes of onions, peppers flavored with crushed coriander seeds and dry fenugreek with hint of cream.</p></div>
    <div class="item"><div class="head"><span>Gosht Biryani 3,5,y</span><span>€11.00</span></div><p>Aged rice cooked with tender land brown onions, home made masala and accompanied with curry sauce.</p></div>
  </div>

  <div class="bar bar--amber" style="left:211px;top:73px;width:176px;height:32px">VEGETARIAN DISHES</div>
  <div class="col" style="left:211px;top:110px;width:176px;height:230px">
    <div class="item"><div class="head"><span>Shahi Paneer 3, 5</span><span>€8.95</span></div><p>Indian cheese in semi-dry sauce.</p></div>
    <div class="item"><div class="head"><span>Subz Maloni Mild.</span><span>€8.95</span></div><p>Stir fried vegetables with ground spices.</p></div>
    <div class="item"><div class="head"><span>Dum Wale Aloo 3</span><span>€8.95</span></div><p>Potatoes cooked with ginger, garlic, onions, yoghurt, &amp; curry leave with cumin Flavored.</p></div>
    <div class="item"><div class="head"><span>Karahi Paneer 3</span><span>€8.95</span></div><p>Colorful curry is prepared using homemade Indian cheese (paneer).</p></div>
    <div class="item"><div class="head"><span>Saag Paneer 3, y,</span><span>€8.95</span></div><p>Pan fried cottage cheese &amp; spinachwith kasoori methi &amp;fresh coriander.</p></div>
    <div class="item"><div class="head"><span>Sambhar Vegetable Curry 4, y v</span><span>€8.95</span></div><p>Vegetable curry cooked with lentil, curry leaves, and mustard seeds.</p></div>
    <div class="item"><div class="head"><span>Vegetable Biryani 3,5,y v</span><span>€8.95</span></div><p>Basmati Rice cooked with vegetables, fresh herbs, spices &amp; fried golden onion. Comes with curry sauce.</p></div>
  </div>

  <div class="bar bar--amber" style="left:211px;top:370px;width:176px;height:32px">NAN BREAD &amp; SIDE ORDERS<br>ALL NAAN BREAD CONTAINS 2,3,6</div>
  <ul class="price-list" style="left:211px;top:406px;width:176px;height:140px">
    <li>Naan<span class="dots"></span><b>€2.20</b></li>
    <li>Garlic Naan<span class="dots"></span><b>€2.50</b></li>
    <li>Garlic Chilli Naan<span class="dots"></span><b>€3.00</b></li>
    <li>Peshwari Naan..5<span class="dots"></span><b>€3.00</b></li>
    <li>Keema Naan<span class="dots"></span><b>€3.00</b></li>
    <li>Coriander Naan<span class="dots"></span><b>€2.50</b></li>
    <li>Chilli Cheese Naan....3<span class="dots"></span><b>€3.00</b></li>
    <li>G.O.C.<span class="dots"></span><b>€3.00</b></li>
    <li>Boiled Basmati<span class="dots"></span><b>€2.00</b></li>
    <li>Pilau Rice<span class="dots"></span><b>€2.00</b></li>
    <li>Lemon Rice........4<span class="dots"></span><b>€3.00</b></li>
    <li>Poppodum(2)<span class="dots"></span><b>€2.50</b></li>
    <li>Riata ....3<span class="dots"></span><b>€2.50</b></li>
  </ul>

  <div class="cover">
    <svg class="abs" width="382" height="548" viewBox="0 0 382 548" role="img" aria-label="Photo of bowls of whole and ground spices">
      <defs>
        <linearGradient id="spice" x1="0" y1="0" x2="1" y2="1">
          <stop offset="0" stop-color="#6b3a24"/>
          <stop offset=".45" stop-color="#c9882c"/>
          <stop offset=".75" stop-color="#a89a48"/>
          <stop offset="1" stop-color="#5a3a22"/>
        </linearGradient>
      </defs>
      <rect width="382" height="548" fill="url(#spice)"/>
      <path d="M0 210 C20 330 110 390 382 400 L382 548 L0 548 Z" fill="#f4b400"/>
      <path d="M0 235 C30 350 120 410 382 418 L382 548 L0 548 Z" fill="#d4262e"/>
    </svg>
    <div class="brand"><span class="brand__name">Saffron Hearth</span><span class="brand__tag">AUTHENTIC INDIAN FOOD AT HOME</span></div>
    <div class="phone">015550192, 015550193</div>
    <div class="web">www.saffronhearth.ie</div>
  </div>
</section>

<section class="sheet sheet--inside">
  <div class="band" style="top:0;height:47px"></div>
  <div class="band" style="top:548px;height:14px"></div>

  <div class="abs hours">
    <h4>OPENING HOURS:</h4>
    <div>Sun &nbsp;&nbsp;- &nbsp;Thurs &nbsp;&nbsp;: 5.00 PM to 10.00PM</div>
    <div>Fri &nbsp;&nbsp;&nbsp;- &nbsp;Sat &nbsp;&nbsp;&nbsp;&nbsp;&nbsp;: 5.00 PM to 10.30PM</div>
    <div><em>Deliveries From 5.30PM</em></div>
    <div>All our meals are cooked to order.</div>
  </div>
  <div class="abs allergens">
    1. Celery 2. Gluten 3. Dairy 4. Mustard 5. Nuts 6. Egg<br>
    7. Fish 8. Soya 9. Penuts 10. Lupin 11. Sulpher Dioxide<br>
    12. Sesame Seeds 13. Molluscs 14. Crustanceans
  </div>

  <div class="abs deals">
    <div class="deals__inner">
      <div class="deals__title"><span>MEAL DEALS</span><strong>ONLY €8.50</strong></div>
      <div class="deals__intro">(Low Fat Dishes<br>Choose with Rice or Plain Naan.</div>
      <div class="col deals__list">
        <div class="item"><div class="head"><span>Chicken Dupiaza</span><span>€8.50</span></div><p>Chicken cooked with ginger and chunks of onions and finished with onion seeds.</p></div>
        <div class="item"><div class="head"><span>Chicken Rogan josh</span><span>€8.50</span></div><p>A red chicken curry prepared with fresh herb &amp; spices, a delicacy from Kashmir.</p></div>
        <div class="item"><div class="head"><span>Chicken Bhuna</span><span>€8.50</span></div><p>Tomatoes and onion sauce cooked with black peppers &amp; spring onions.</p></div>
        <div class="item"><div class="head"><span>Tarkari Makhani 3,5</span><span>€8.50</span></div><p>Mixed seasonal vegetables in a smooth tikka masala sauce.</p></div>
      </div>
    </div>
    <div class="set" style="top:186px"><div class="head"><span>Set Meal 1 ..................................</span><span>€16.00</span></div>
      <div class="cols"><div>- Onion bhajia<br>- Chicken Tikka Masala<br>- Pilau rice</div><div>- Naan<br>- Poppadoms</div></div></div>
    <div class="set" style="top:233px"><div class="head"><span>Set Meal For 2..........................</span><span>€27.00</span></div>
      <div class="cols"><div>- Onion bhajia<br>- Chicken tikka<br>- Chicken Tikka Masala<br>- Lamb Roganjosh</div><div>- 2xPilau rice<br>- 1xNaan<br>- Poppadom</div></div></div>
    <div class="set" style="top:288px"><div class="head"><span>Set Meal for 3/4.........................</span><span>€43.00</span></div>
      <div class="cols"><div>- Onion Bhajia<br>- Vegetable Samosa<br>- Chicken Tikka<br>- Chicken Tikka Masala<br>- Lamb Roganjosh</div><div>- Sambhar Veg Curry<br>- 2 x Pilau Rice<br>- 2xPilau rice<br>- Poppadom</div></div></div>
  </div>

  <div class="photo" style="left:197px;top:57px;width:200px;height:161px;background:linear-gradient(135deg,#8b8f93 0%,#c0652a 35%,#e2c27a 60%,#9bb04a 85%,#6f7a3a 100%)" role="img" aria-label="Photo of a thali plate with curry, rice and poppadom"></div>

  <div class="bar bar--green" style="left:202px;top:226px;width:191px;height:31px">HEALTHY &nbsp;SIDE ORDERS</div>
  <div class="col" style="left:202px;top:262px;width:191px;height:220px">
    <div class="item"><div class="head"><span>Sautéed Broccoli &nbsp;&nbsp;&nbsp;&nbsp;&nbsp;v</span><span>€5.00</span></div><p>Broccoli, green beans and spinach leaves sautéed with roasted cumin and fresh garlic.</p></div>
    <div class="item"><div class="head"><span>Chana Saag &nbsp;3 &nbsp;&nbsp;yv</span><span>€5.00</span></div><p>Chickpeas cooked with chopped spinach, onion, and cumin and finished with cream.</p></div>
    <div class="item"><div class="head"><span>Chana Masala &nbsp;&nbsp;&nbsp;&nbsp;v</span><span>€5.00</span></div><p>Chickpeas simmered with tomato, caramelised onion, black pepper and fresh coriander.</p></div>
    <div class="item"><div class="head"><span>Aloo Saag &nbsp;&nbsp;3 &nbsp;&nbsp;yv</span><span>€5.00</span></div><p>Crispy Potato with spinach, caramelised onion, garam masala and a dash of cream.</p></div>
    <div class="item"><div class="head"><span>Aloo Ghobhi &nbsp;&nbsp;&nbsp;&nbsp;v</span><span>€5.00</span></div><p>Crispy Potatoes cubes &amp; Cauliflower cooked with roasted cumin with tomato and onion gravy.</p></div>
    <div class="item"><div class="head"><span>Tarka Daal &nbsp;&nbsp;&nbsp;4 &nbsp;&nbsp;yv</span><span>€5.00</span></div><p>Home style soaked yellow chana cooked with cumin &amp; garam masala.</p></div>
    <div class="item"><div class="head"><span>Tangy Aloo &nbsp;&nbsp;&nbsp;v</span><span>€5.00</span></div><p>Crispy Potatoes cubes cooked with roasted cumin and touch of our tangy sauce</p></div>
  </div>
  <div class="abs legend">Y &nbsp;: can be cooked without allergen<br>H &nbsp;: Healthy Option<br>V &nbsp;: Suitable for Vegans</div>

  <div class="bar bar--red" style="left:405px;top:71px;width:191px;height:32px">STARTERS</div>
  <div class="col" style="left:405px;top:108px;width:191px;height:427px">
    <div class="item"><div class="head"><span>Onion Bhajia</span><span>€4.50</span></div><p>Spinach &amp; onions fritters flavored with mild spices.</p></div>
    <div class="item"><div class="head"><span>Vegetable Samosa &nbsp;&nbsp;2</span><span>€4.50</span></div><p>Crispy Pastry stuffed with potatoes, chick peas, Green peas mixed with desi spices until golden.</p></div>
    <div class="item"><div class="head"><span>Palak Tikki</span><span>€4.50</span></div><p>Cakes of fresh spinach and chana dal.</p></div>
    <div class="item"><div class="head"><span>Veg Pakora</span><span>€5.00</span></div><p>Cauliflower, potato and broccoli, golden fried with Gram flour batter.</p></div>
    <div class="item"><div class="head"><span>Keema Singhara 2</span><span>€5.00</span></div><p>Spicy seasoned mince lamb in light pastryed with egg, green peas &amp; onion served with curry sauce.</p></div>
    <div class="item"><div class="head"><span>Chicken Tikka 3</span><span>€5.00</span></div><p>Tender chicken marinated overnight with yoghurt, spices charred in tandoor.</p></div>
    <div class="item"><div class="head"><span>Seekh Kebab</span><span>€5.50</span></div><p>Skewered hand pounder lamb glazed in tandoor with green chilli &amp; black cardamom.</p></div>
    <div class="item"><div class="head"><span>Chicken Pakora</span><span>€5.00</span></div><p>Boneless pieces of chicken coated in gram flour batter, with spices.</p></div>
    <div class="item"><div class="head"><span>Chicken Wings &nbsp;&nbsp;2,1</span><span>€5.00</span></div></div>
    <div class="item"><div class="head"><span>Tandoori Mix Meat Platter 3</span><span>€9.50</span></div><p>Our special tandoori assortment of tandoori chicken on bone, seekh kebab and chicken tikka.</p></div>
    <div class="item"><div class="head"><span>Mix Veg platter 2</span><span>€6.50</span></div><p>Veg Samosa, Onion Bhaji, Veg Pakora.</p></div>
    <div class="item"><div class="head"><span>Doner Kebab 2,3,6</span><span>€8.00</span></div><p>Stripes of minced chicken &amp; beef served with garlic mayo, chilli sauce &amp; mixed salad &amp; wrapped in naan.</p></div>
    <div class="item"><div class="head"><span>Chicken Tikka Kebab 2,3,6</span><span>€8.00</span></div><p>Chicken breast marinated in spices, barbecued served with garlic mayo, chilli sauce &amp; mixed salad &amp; wrapped in naan.</p></div>
  </div>

  <div class="col" style="left:605px;top:72px;width:181px;height:39px">
    <div class="item"><div class="head"><span>Mix Kebab 2,3,6</span><span>€8.00</span></div><p>Pieces of chicken tikka &amp; donner meat with garlic mayo, sweet chilli &amp; salad wrapped in naan bread.</p></div>
    <div class="item"><div class="head"><span>Garlic Chips</span><span>€4.00</span></div></div>
  </div>

  <div class="bar bar--red" style="left:605px;top:118px;width:181px;height:32px">CHEF RAVI'S SPECIAL CURRIES</div>
  <div class="col" style="left:605px;top:156px;width:181px;height:165px">
    <div class="item"><div class="head"><span>Butter Murgh &nbsp;&nbsp;&nbsp;&nbsp;&nbsp;3,5</span><span>€10.50</span></div><p>Chicken cooked in tandoor mixed with rich Tomato creamy cashew sauce, splash of cream with hint of honey &amp; dry fenugreek.</p></div>
    <div class="item"><div class="head"><span>Laal Maas</span><span>€11.50</span></div><p>Taditional rajasthani lamb cooked with garlic and ginger , degi chilli powder, tomatoes finished with star aniseed and clove powder.</p></div>
    <div class="item"><div class="head"><span>Shahi Veg Kofta 3'5</span><span>€10.00</span></div><p>Handmade veg and panner dumplings simmered in tomato sauce, musky fenugreek sauce finished with touch of honey and cream.</p></div>
    <div class="item"><div class="head"><span>Kerala Prawn 14</span><span>€12.00</span></div><p>Delicacy of kerala spices, tomato and red onion gravy finished with touch of fresh coconut milk.</p></div>
  </div>

  <div class="bar bar--red" style="left:605px;top:329px;width:181px;height:32px">CHICKEN DISHES</div>
  <div class="col" style="left:605px;top:367px;width:181px;height:165px">
    <div class="item"><div class="head"><span>Butter Murgh &nbsp;&nbsp;&nbsp;&nbsp;&nbsp;3,5</span><span>€10.50</span></div><p>Chicken cooked in tandoor mixed with rich Tomato creamy cashew sauce, splash of cream with hint of honey &amp; dry fenugreek.</p></div>
    <div class="item"><div class="head"><span>Laal Maas</span><span>€11.50</span></div><p>Taditional rajasthani lamb cooked with garlic and ginger , degi chilli powder, tomatoes finished with star aniseed and clove powder.</p></div>
    <div class="item"><div class="head"><span>Shahi Veg Kofta 3'5</span><span>€10.00</span></div><p>Handmade veg and panner dumplings simmered in tomato sauce, musky fenugreek sauce finished with touch of honey and cream.</p></div>
    <div class="item"><div class="head"><span>Kerala Prawn 14</span><span>€12.00</span></div><p>Delicacy of kerala spices, tomato and red onion gravy finished with touch of fresh coconut milk.</p></div>
  </div>
</section>

</body>
</html>
```